Project Folder

We are a modern Cosmetics supplier looking for a (FRESH/TRENDY/MODERN) paper project folder.

I have included a example that we really like as it is plain and totally cool!
Let's work from this EXAMPLE except using our company products from our web page (www.lurovexa.ca)

Target Market(s)

Women

Colors
ec2027

Requirements
Must have
• Clean look
Red Company web address

```html
<!DOCTYPE html>
<html lang="en">
<head>
<meta charset="utf-8">
<title>Lurovexa Project Folder</title>
<link href="https://fonts.googleapis.com/css2?family=Quicksand:wght@400;500;700&display=swap" rel="stylesheet">
<style>
  :root {
    --bg: #ffffff;
    --page: #ffffff;
    --red: #ec2027;
    --pink: #e8207e;
    --yellow: #f4c419;
    --purple: #7b3fe4;
    --teal: #5fe0cf;
    --rule: #c9c9c9;
    --edge: #e2e2e2;
    --mark: #d6d6d6;
  }
  * { box-sizing: border-box; margin: 0; padding: 0; }
  html, body { width: 888px; height: 1200px; overflow: hidden; background: var(--bg); }
  body { position: relative; font-family: "Quicksand", sans-serif; color: var(--pink); }

  .page {
    position: absolute;
    background: var(--page);
    border: 1px solid var(--edge);
    overflow: hidden;
  }
  .back-cover  { left: 74px;  top: 50px;  width: 366px; height: 517px; }
  .front-cover { left: 448px; top: 50px;  width: 366px; height: 517px; }
  .inside-left { left: 79px;  top: 627px; width: 366px; height: 516px; }
  .inside-right{ left: 448px; top: 627px; width: 366px; height: 516px; }

  .web-address {
    position: absolute;
    left: 36px; top: 318px;
    transform: rotate(-90deg);
    transform-origin: left top;
    font-size: 21px;
    font-weight: 400;
    letter-spacing: 0.3px;
    color: var(--red);
    white-space: nowrap;
  }

  .brand {
    position: absolute;
    left: 58px; top: 118px;
    display: flex; align-items: center; gap: 5px;
    font-size: 13px; font-weight: 700; color: var(--pink);
  }
  .brand-dot { width: 14px; height: 14px; border-radius: 50%; background: var(--pink); }

  .hero-visual {
    position: absolute;
    left: 78px; top: 143px;
    width: 222px; height: 310px;
    border-radius: 6px;
    background: linear-gradient(180deg, #5fcfc6 0%, #5fcfc6 22%, #e63fb0 28%, #e63fb0 46%, #f1c428 52%, #f1c428 70%, #8a4fe0 76%, #8a4fe0 100%);
    opacity: 0.85;
  }

  .intro {
    position: absolute;
    left: 35px; top: 35px;
    font-size: 11.5px; line-height: 14px; font-weight: 500;
    color: var(--pink);
  }
  .intro strong { font-weight: 700; }

  .product-visual {
    position: absolute;
    left: 81px; top: 173px;
    width: 210px; height: 176px;
    border-radius: 4px;
    background: linear-gradient(180deg, #eef3ee 0%, #cfe6cc 55%, #8fc98a 100%);
  }

  .partner-row {
    position: absolute;
    left: 26px; top: 489px;
    display: flex; gap: 14px; align-items: center;
  }
  .partner-mark { width: 28px; height: 11px; background: var(--mark); border-radius: 2px; }

  .tagline-frame {
    position: absolute;
    left: 87px; top: 173px;
    width: 280px; height: 344px;
    border: 1px solid var(--rule);
  }
  .tagline {
    position: absolute;
    left: 107px; top: 81px;
    font-weight: 400;
    line-height: 1;
  }
  .tagline-lead {
    display: block;
    font-size: 24px; font-weight: 400; line-height: 30px;
    color: var(--pink); text-transform: uppercase;
  }
  .tagline-people {
    display: block;
    margin-top: 8px;
    font-size: 46px; font-weight: 700; line-height: 46px;
    color: var(--pink);
    letter-spacing: 0.5px;
  }
  .tagline-love {
    display: block;
    margin-top: -2px;
    font-size: 66px; font-weight: 400; line-height: 66px;
    letter-spacing: 0.5px;
  }
  .love-l { color: var(--yellow); }
  .love-o { color: var(--purple); }
  .love-v { color: var(--pink); }
  .love-e { color: var(--teal); }
</style>
</head>
<body>
  <section class="page back-cover">
    <p class="web-address">www.lurovexa.ca</p>
  </section>

  <section class="page front-cover">
    <div class="brand"><span class="brand-dot"></span>Lurovexa</div>
    <div class="hero-visual" role="img" aria-label="Stack of four open nail polish bottles in teal, pink, yellow and purple with dripping polish"></div>
  </section>

  <section class="page inside-left">
    <p class="intro">The <strong>European</strong> cosmetics<br>industry is a world <strong>leader</strong><br>and dominant <strong>cosmetics</strong><br>exporter</p>
    <div class="product-visual" role="img" aria-label="Aloe skincare products: sheet mask, tube and jar"></div>
    <div class="partner-row" aria-label="Partner brands">
      <span class="partner-mark"></span>
      <span class="partner-mark"></span>
      <span class="partner-mark"></span>
      <span class="partner-mark"></span>
      <span class="partner-mark"></span>
    </div>
  </section>

  <section class="page inside-right">
    <div class="tagline-frame"></div>
    <h1 class="tagline">
      <span class="tagline-lead">European<br>products<br>that</span>
      <span class="tagline-people">PEOPLE</span>
      <span class="tagline-love"><span class="love-l">L</span><span class="love-o">O</span><span class="love-v">V</span><span class="love-e">E</span></span>
    </h1>
  </section>
</body>
</html>
```